QRV In Home Flier

To prepare a flier to be placed directly into existing clients homes, which shares additional services available. These are clients that are using QRV Cleaning services and we want to use our QRV Pest Control or BWO (Bondo Mend Up)Maintenance Services

Target Market(s)

residential home owners / Renters

Industry/Entity Type

Property Maintenance

Colors

Designer to choose colors to be used in the design.

Requirements
Must have
• Must be crisp and clean - design should pop - A CLEAR call to action
Nice to have
• See previous designed uploaded
Should not have

```html
<!DOCTYPE html>
<html lang="en">
<head>
<meta charset="utf-8">
<title>QRV In Home Fliers</title>
<link href="https://fonts.googleapis.com/css2?family=Open+Sans:wght@400;600;700;800&display=swap" rel="stylesheet">
<style>
  :root {
    --page-bg: #d9d9d9;
    --paper: #ffffff;
    --slate: #5d6680;
    --slate-dark: #4a5269;
    --sky: #3a8fc8;
    --sun: #ece12b;
    --ink: #1d1d1d;
    --panel-grey: #d4d6da;
    --panel-light: #eeeeee;
    --leaf: #8cc63f;
  }
  * { box-sizing: border-box; margin: 0; padding: 0; }
  html, body { width: 1200px; height: 1000px; overflow: hidden; }
  body {
    background: var(--page-bg);
    font-family: "Open Sans", Arial, sans-serif;
    color: var(--ink);
    position: relative;
  }
  .flier {
    position: absolute;
    top: 170px;
    width: 500px;
    height: 660px;
    background: var(--paper);
    overflow: hidden;
    box-shadow: 0 6px 18px rgba(0,0,0,0.18);
  }
  .flier--cleaning { left: 70px; }
  .flier--pest { left: 630px; }

  .hero-photo {
    position: absolute; left: 0; top: 0; width: 100%; height: 320px;
  }
  .flier--cleaning .hero-photo {
    background: linear-gradient(160deg, #f4f4f2 0%, #e7e3dc 45%, #d8d2c6 75%, #c7b9a2 100%);
  }
  .flier--pest .hero-photo {
    background: linear-gradient(120deg, #d9dde2 0%, #eef0f3 40%, #b9bcc2 65%, #5a3a30 100%);
  }

  .brand-mark {
    position: absolute; left: 22px; top: 60px;
    display: flex; align-items: center; gap: 8px;
    font-weight: 700; font-size: 26px; color: var(--slate-dark);
    letter-spacing: 1px;
  }
  .brand-mark .brand-square {
    width: 26px; height: 26px; background: var(--slate-dark);
  }

  .cta-box {
    position: absolute; right: 0; top: 232px;
    width: 230px; height: 118px;
    background: var(--sun);
    clip-path: polygon(14% 0, 100% 0, 100% 100%, 0 100%);
    text-align: center;
    padding: 12px 10px 0 40px;
    line-height: 1.1;
  }
  .cta-box .cta-lead { font-size: 17px; font-weight: 400; }
  .cta-box .cta-number {
    display: flex; align-items: center; justify-content: center; gap: 6px;
    font-size: 34px; font-weight: 800; margin-top: 4px;
  }
  .cta-box .cta-number svg { width: 26px; height: 26px; }
  .cta-box .cta-word { font-size: 22px; font-weight: 400; letter-spacing: 1px; }

  .service-banner {
    position: absolute; left: 0; top: 265px;
    width: 320px; height: 140px;
    clip-path: polygon(0 0, 88% 0, 100% 50%, 88% 100%, 0 100%);
    color: #fff; padding: 14px 30px 0 30px;
    line-height: 1.22;
  }
  .flier--cleaning .service-banner { background: var(--slate); }
  .flier--pest .service-banner { background: var(--sky); }
  .service-banner h2 { font-size: 18px; font-weight: 400; letter-spacing: 0.5px; margin-bottom: 4px; }
  .service-banner p { font-size: 16px; }
  .service-banner .small { font-size: 14px; padding-left: 14px; }
  .service-banner .motto { font-size: 17px; margin-top: 4px; }

  .side-photo {
    position: absolute; right: 30px; top: 360px; width: 150px; height: 110px;
    background: linear-gradient(135deg, #b7e06a, var(--leaf) 60%, #6ea22c);
  }

  .services {
    position: absolute; left: 40px; top: 410px;
  }
  .services h3 { font-size: 17px; font-weight: 800; margin-bottom: 2px; line-height: 1.3; }
  .services li {
    list-style: none; font-size: 16px; line-height: 1.4;
    display: flex; align-items: center; gap: 10px;
  }
  .services li svg { width: 14px; height: 12px; flex: none; }

  .mascot-art {
    position: absolute; left: 255px; top: 420px; width: 90px; height: 100px;
    background: linear-gradient(180deg, #e6e6e6, #9a9a9a);
  }
  .pest-name {
    position: absolute; left: 350px; top: 448px;
    display: flex; align-items: center; gap: 6px;
    font-size: 20px; font-weight: 400; color: var(--sky); line-height: 1.05;
  }
  .pest-name .brand-square { width: 16px; height: 16px; background: var(--sky); flex: none; }

  .info-panel {
    position: absolute; left: 0; width: 100%;
  }
  .flier--cleaning .info-panel {
    top: 538px; height: 105px;
    padding: 8px 36px;
    background: linear-gradient(180deg, var(--panel-light), var(--panel-grey));
  }
  .flier--pest .info-panel {
    top: 552px; height: 91px;
    padding: 8px 36px;
    background: var(--sun);
  }
  .info-panel h4 { font-size: 16px; font-weight: 600; margin-bottom: 2px; line-height: 1.35; }
  .info-panel p { font-size: 11px; line-height: 1.3; }
  .flier--pest .info-panel p { font-size: 13px; font-weight: 600; line-height: 1.25; margin-bottom: 4px; }

  .base-strip {
    position: absolute; left: 0; bottom: 0; width: 100%; height: 17px;
    background: var(--slate);
  }
</style>
</head>
<body>
  <svg width="0" height="0" style="position:absolute">
    <defs>
      <symbol id="chevrons" viewBox="0 0 14 12">
        <path d="M1 1 L6 6 L1 11 M7 1 L12 6 L7 11" fill="none" stroke="#2b3550" stroke-width="2"/>
      </symbol>
      <symbol id="phone" viewBox="0 0 26 26">
        <circle cx="13" cy="13" r="11.5" fill="none" stroke="#1d1d1d" stroke-width="2.2"/>
        <path d="M8.5 7.5 c1-1 2-1 2.6 0 l1 2 c0.4 0.8 0 1.4-0.6 1.9 c0.8 1.8 2 3 3.8 3.8 c0.5-0.6 1.1-1 1.9-0.6 l2 1 c1 0.6 1 1.6 0 2.6 c-1.2 1.2-3 1.4-5 0.2 c-2.4-1.4-4.3-3.3-5.7-5.7 c-1.2-2-1-3.800.2-5.2z" fill="#1d1d1d"/>
      </symbol>
    </defs>
  </svg>

  <article class="flier flier--cleaning">
    <div class="hero-photo" role="img" aria-label="Photo of a person steam-mopping a bright living room floor beside a sofa with yellow cushions"></div>
    <div class="brand-mark"><span class="brand-square"></span>QRV</div>

    <div class="cta-box">
      <div class="cta-lead">Call us now<br>for a free estimate!</div>
      <div class="cta-number"><svg><use href="#phone"/></svg>800</div>
      <div class="cta-word">SPARKLE</div>
    </div>

    <div class="service-banner">
      <h2>HOME CLEANING SERVICE</h2>
      <p>Domestic Helper on leave?<br>Need a part-time cleaner?<br>Call our maids for help today!<br>QRV HOME HELP</p>
    </div>

    <div class="side-photo" role="img" aria-label="Photo of a clean lime-green living room interior"></div>

    <div class="services">
      <h3>OUR SERVICES</h3>
      <ul>
        <li><svg><use href="#chevrons"/></svg>Same maid everytime</li>
        <li><svg><use href="#chevrons"/></svg>Ironing</li>
        <li><svg><use href="#chevrons"/></svg>In-house training facility</li>
        <li><svg><use href="#chevrons"/></svg>Laundry</li>
      </ul>
    </div>

    <div class="info-panel">
      <h4>PROFESSIONAL CLEANING SERVICE</h4>
      <p>QRV Home Help is one of the only cleaning companies to be endorsed by the UAE government. This is because we look after our maids properly and have even built our own in house training facility to make sure that you only receive maids that are qualified to be in your home.</p>
    </div>
    <div class="base-strip"></div>
  </article>

  <article class="flier flier--pest">
    <div class="hero-photo" role="img" aria-label="Photo of a pest control worker in a white protective suit spraying along a kitchen floor"></div>
    <div class="brand-mark"><span class="brand-square"></span>QRV</div>

    <div class="cta-box">
      <div class="cta-lead">Call us now<br>for a free estimate!</div>
      <div class="cta-number"><svg><use href="#phone"/></svg>800</div>
      <div class="cta-word">SPARKLE</div>
    </div>

    <div class="service-banner">
      <h2>PEST CONTROL SERVICE</h2>
      <p class="small">-European managed<br>-monthly - quarterly - annually<br>&nbsp;maintenance contracts<br>-On call service</p>
      <p class="motto">Your property, our priority.</p>
    </div>

    <div class="services">
      <h3>OUR SERVICES</h3>
      <ul>
        <li><svg><use href="#chevrons"/></svg>General Pest Control</li>
        <li><svg><use href="#chevrons"/></svg>Bed Bugs Control</li>
        <li><svg><use href="#chevrons"/></svg>Rat Control</li>
        <li><svg><use href="#chevrons"/></svg>Cockroaches Control</li>
        <li><svg><use href="#chevrons"/></svg>Ant Control</li>
      </ul>
    </div>

    <div class="mascot-art" role="img" aria-label="Cartoon of a pest control worker chasing a bug"></div>
    <div class="pest-name"><span class="brand-square"></span>QRV<br>Pest Control</div>

    <div class="info-panel">
      <p>QRV Pest Control is reinventing the pest control service industry in Dubai.</p>
      <p>This means you get the right Pest Control Workers, with the right tools at the right time!</p>
    </div>
    <div class="base-strip"></div>
  </article>
</body>
</html>
```